New London Job Board - Business Card Required

Dear All,

I own Quintaro Limited, which in turn owns the website:
www.brambletopfield.com

I want all of you wonderful creative people to come up with a slick, and awesome business card design that incorporates the logo on the site, and some colouring and design elements from it.

You have free reign in how you go about doing this, I won't be giving my contact details on this platform, but the winner will be asked to redesign based on my contact details which I will supply at the end.

I need the design to be completed within 5 days. I need the final print copies of the business cards by the 25th November, so unfortunately it's a bit of a rush to get these designs ready.

Any questions, please ask.

Thank you

Thank you all for your hard work and exceptional designs provided. I do have to pick one, so I have a very clear idea of which one this is, however I will wait one further day until the competition closes to be fair to all those have submitted, or are in the process of submitting. I wish you all the best and thank you again for your dedication.

```html
<!DOCTYPE html>
<html lang="en">
<head>
<meta charset="utf-8">
<title>Brambletop Field — Business Card</title>
<link rel="stylesheet" href="https://fonts.googleapis.com/css2?family=Fira+Sans:wght@400;600&display=swap">
<style>
  :root {
    --backdrop: #e9e6e1;
    --card: #2a2829;
    --gold: #c9a24a;
    --gold-light: #dcbb6a;
  }
  * { box-sizing: border-box; margin: 0; padding: 0; }
  html, body {
    width: 1200px;
    height: 800px;
    overflow: hidden;
    background: var(--backdrop);
    font-family: "Fira Sans", Arial, sans-serif;
  }
  .stage {
    position: relative;
    width: 1200px;
    height: 800px;
  }
  .card {
    position: absolute;
    top: 232px;
    width: 520px;
    height: 336px;
    background: var(--card);
    box-shadow: 0 6px 18px rgba(0,0,0,0.25);
  }
  .card--front { left: 50px; }
  .card--back  { left: 630px; }

  .card__frame {
    position: absolute;
    border: 2px solid var(--gold);
  }
  .card--front .card__frame { inset: 34px 34px 34px 34px; }
  .card--back .card__frame  { inset: 26px 26px 26px 26px; }

  /* Front: brand name */
  .brand {
    position: absolute;
    inset: 0;
    display: flex;
    flex-direction: column;
    align-items: center;
    justify-content: center;
    gap: 16px;
  }
  .brand__dot {
    width: 54px;
    height: 54px;
    border-radius: 50%;
    background: var(--gold);
  }
  .brand__name {
    color: var(--gold);
    font-weight: 400;
    font-size: 30px;
    letter-spacing: 3px;
    text-transform: uppercase;
  }

  /* Back: person */
  .person {
    position: absolute;
    top: 44px;
    right: 48px;
    text-align: right;
    color: var(--gold-light);
  }
  .person__name {
    font-weight: 600;
    font-size: 19px;
  }
  .person__role {
    font-weight: 400;
    font-size: 15px;
    margin-top: 2px;
  }

  /* Back: contact list */
  .contacts {
    position: absolute;
    left: 48px;
    bottom: 44px;
    list-style: none;
    color: var(--gold-light);
    font-size: 13.5px;
    line-height: 1.3;
  }
  .contacts__item {
    display: flex;
    align-items: flex-start;
    gap: 10px;
    margin-top: 7px;
  }
  .contacts__icon {
    flex: none;
    width: 13px;
    height: 13px;
    margin-top: 2px;
  }
</style>
</head>
<body>
<main class="stage">

  <section class="card card--front" aria-label="Business card front">
    <div class="card__frame"></div>
    <div class="brand">
      <div class="brand__dot"></div>
      <div class="brand__name">Brambletop Field</div>
    </div>
  </section>

  <section class="card card--back" aria-label="Business card back">
    <div class="card__frame"></div>

    <div class="person">
      <div class="person__name">Idris Marlow</div>
      <div class="person__role">Managing Director</div>
    </div>

    <ul class="contacts">
      <li class="contacts__item">
        <svg class="contacts__icon" viewBox="0 0 13 13" aria-hidden="true">
          <rect width="13" height="13" rx="2" fill="#c9a24a"/>
          <path d="M6.5 2.3a2.7 2.7 0 0 0-2.7 2.7c0 2 2.7 5.2 2.7 5.2s2.7-3.2 2.7-5.2a2.7 2.7 0 0 0-2.7-2.7z" fill="#2a2829"/>
          <circle cx="6.5" cy="5" r="1" fill="#c9a24a"/>
        </svg>
        <span>Brambletop Field c/o Quintaro Limited<br>17 Calder Row, Westfield, Norbury, N4R 2TL.</span>
      </li>
      <li class="contacts__item">
        <svg class="contacts__icon" viewBox="0 0 13 13" aria-hidden="true">
          <rect width="13" height="13" rx="2" fill="#c9a24a"/>
          <path d="M4 2.8l1.5 1.9-.8 1c.5 1 1.2 1.7 2.2 2.2l1-.8 1.9 1.5-.9 1.4C6.6 9.8 3.2 6.4 2.9 4.1z" fill="#2a2829"/>
        </svg>
        <span>0000 000 000</span>
      </li>
      <li class="contacts__item">
        <svg class="contacts__icon" viewBox="0 0 13 13" aria-hidden="true">
          <rect width="13" height="13" rx="2" fill="#c9a24a"/>
          <rect x="2.5" y="3.8" width="8" height="5.4" fill="#2a2829"/>
          <path d="M2.5 3.8l4 3 4-3" fill="none" stroke="#c9a24a" stroke-width="0.9"/>
        </svg>
        <span>contact@brambletopfield.com</span>
      </li>
    </ul>
  </section>

</main>
</body>
</html>
```